We need an attractive, simple & modern / Aussie Design of BusinessCard using the existing company Logo.
Our company is located in Perth, WA, Australia.
The Company name is Tarn Vale Construction & Maintenance
Name on the card is Dorian Pelk
Designation is Managing Director
Building Registration BC584731
M: 0438 517 362
E: tarnvaleconstruction@mailhub.example

Our main tasks are Building new homes, medical centers, mixed use. Renovations & Maintenance.

Slogan: Let Quality Meets Your Budget (We are open if you please suggest something more attractive within same concept)

Target Market(s)

Individuals to build or renovate homes, Doctors and dentists to build, renovate, fit off clinics and medical centres, Schools & real estate offices for maintenance contracts.

Industry/Entity Type

Construction

Contact Information for Business Card

To contain company name, logo, person name and contact details, building registration detail, slogan and to give brief on our services

Colors

Designer to choose colors to be used in the design.

Requirements
Must have
• To have attractive design. And contain company name, logo, person name, designation and contact details, building registration detail, slogan and to give brief on our services.
• Elegant and Simple Style.
Nice to have
• Modern Aussie style.
Should not have
• Should not be too much busy or complicated.

```html
<!DOCTYPE html>
<html lang="en">
<head>
<meta charset="utf-8">
<title>Tarn Vale Construction &amp; Maintenance – Business Card</title>
<link rel="stylesheet" href="https://fonts.googleapis.com/css2?family=Michroma&display=swap">
<style>
  :root {
    --backdrop: #bcbdbf;
    --card: #ffffff;
    --orange: #f47321;
    --ink: #050608;
    --shadow: rgba(0, 0, 0, 0.45);
    --type: "Michroma", sans-serif;
  }
  * { margin: 0; padding: 0; box-sizing: border-box; }
  html, body {
    width: 1200px;
    height: 1000px;
    overflow: hidden;
    background: var(--backdrop);
    font-family: var(--type);
  }
  .card {
    position: absolute;
    left: 279px;
    width: 642px;
    height: 376px;
    background: var(--card);
    box-shadow: 6px 6px 6px var(--shadow);
    overflow: hidden;
  }
  .card--front { top: 113px; }
  .card--back { top: 511px; }
  .card__art {
    position: absolute;
    inset: 0;
    width: 642px;
    height: 376px;
  }
  .stripe { fill: var(--orange); }
  .contact-band { fill: var(--ink); }

  .brand {
    position: absolute;
    left: 0;
    width: 642px;
    text-align: center;
    color: var(--ink);
  }
  .brand__mark {
    display: block;
    width: 44px;
    height: 44px;
    margin: 0 auto 14px;
    background: var(--orange);
  }
  .brand__name {
    display: block;
    font-size: 27px;
    line-height: 1;
    letter-spacing: 0.5px;
  }
  .brand__tagline {
    display: block;
    font-size: 8.6px;
    line-height: 1;
    margin-top: 5px;
    letter-spacing: 0.3px;
  }
  .card--front .brand { top: 98px; }
  .card--back .brand { top: 163px; }

  .person {
    position: absolute;
    top: 208px;
    left: 0;
    width: 642px;
    text-align: center;
  }
  .person__name {
    font-size: 25px;
    line-height: 1;
    color: var(--ink);
    letter-spacing: 0.5px;
  }
  .person__role {
    margin-top: 10px;
    font-size: 13px;
    line-height: 1;
    color: var(--orange);
  }

  .contact {
    position: absolute;
    top: 294px;
    left: 0;
    width: 642px;
    text-align: center;
    list-style: none;
    color: var(--orange);
  }
  .contact__item {
    font-size: 13px;
    line-height: 18.5px;
  }
  .contact__item--email { font-size: 10.5px; }
</style>
</head>
<body>

<section class="card card--front" aria-label="Business card front">
  <svg class="card__art" viewBox="0 0 642 376" aria-hidden="true">
    <polygon class="contact-band" points="118,275 524,275 570,376 73,376"/>
    <polygon class="stripe" points="242,0 247,0 0,269 0,172"/>
    <polygon class="stripe" points="242,0 247,0 73,376 9,376"/>
    <polygon class="stripe" points="399,0 404,0 642,172 642,269"/>
    <polygon class="stripe" points="399,0 404,0 633,376 570,376"/>
  </svg>

  <div class="brand">
    <span class="brand__mark"></span>
    <span class="brand__name">TARN VALE</span>
    <span class="brand__tagline">CONSTRUCTION &amp; MAINTENANCE</span>
  </div>

  <div class="person">
    <p class="person__name">Dorian Pelk</p>
    <p class="person__role">Managing Director</p>
  </div>

  <ul class="contact">
    <li class="contact__item">BC584731</li>
    <li class="contact__item">0438 517 362</li>
    <li class="contact__item contact__item--email">tarnvaleconstruction@mailhub.example</li>
  </ul>
</section>

<section class="card card--back" aria-label="Business card back">
  <div class="brand">
    <span class="brand__mark"></span>
    <span class="brand__name">TARN VALE</span>
    <span class="brand__tagline">CONSTRUCTION &amp; MAINTENANCE</span>
  </div>
</section>

</body>
</html>
```